依頼詳細
【サイトマップ】
TOPページ
---HOME
---COMPANY (会社概要/会社沿革)
---BUSINESS (事業内容)
---RECRUIT  (採用情報)
---CONTACT  (問い合わせ)
---NEWS  (新着情報)
【サイト作成においてのポイント】
・レスポンシブデザインでお願いいたします。
・各所の素材は全てURLをお送り下さい。

【イメージ全体配置構図(いれていただきたい要素)】

ワイヤーフレームをご確認ください。
①~⑧までワイヤーフレーム内にふった番号順に詳細を記載しております。

※ワイヤーフレームはあくまでも入れたい要素を並べた一例になります。
各配置、表示位置は変えていただいても問題ございません。
------------------------

①グローバルナビ
配置は上部でお願いいたします。位置は中央を希望いたします。
------

②メインビジュアル
メインビジュアルは動画(アニメーション)挿入の仕様想定で作成して頂きたいです。
参考サイト:http://www.kovtel-sample.com/
http://info.harumiwave-sample.jp/

1ページまるごと動画(アニメーション)仕様でも問題ございません。
参考サイト:http://www.quistfold-sample.com/

(こちらでは素材を用意しておりません。確認後、購入手続きをさせていただきますのでURLをお送りください)
サイズはどのデバイスでも横幅が100%になるように考えております。
縦幅はお任せしますので、素材にあわせていただけますと幸いです。
------

③新着情報
新着情報は3つ以上いれていただけますと幸いです
いれていただきたい要素は
・更新日時(年,月,日)
・更新内容のテキスト部分 20文字前後

各テキストの配置箇所、文字色、フォント、文字やボタンのサイズ、幅感等の指定はございません。
ワイヤーフレームにはいれていただきたい要素だけならべています。
------

④事業紹介箇所
入れていただきたい要素は以下になります。
・事業紹介イメージ素材
メイン動画がヘッダー部分のみに表示の場合
背景画像として、サイズは横が100%になるように考えております。
メイン動画が全体の場合
イメージ素材が浮き上がってくるようなアニメーション仕様で考えておりますので、その仕様にあったサイズ、表示方法にしていただけますと幸いです。

極力どのデバイスサイズでもバランスよく見えるような素材をご使用いただけますと幸いです。

・事業内容の名前
(Internet media、Promotion、Influencer Marketing)
・以下テキスト
(MiraKestelはインターネットを軸とした事業を展開しております。)
・下層ページへのリンクボタン

------

⑤入れていただきたい要素は以下になります。
・背景素材
メイン動画がヘッダー部分のみに表示の場合
メイン動画が全体の場合

・遷移先の中に含まれる内容の紹介
(Staff Interview、One Day、Blog)
・以下テキスト
(MiraKestelの福利厚生や、メンバーの1日の勤務スケジュールを公開)
・下層ページへのリンクボタン

------

⑥入れていただきたい要素は以下になります。
・背景素材
メイン動画がヘッダー部分のみに表示の場合
メイン動画が全体の場合

・遷移先の中に含まれる内容の紹介
(overview/ history、Greeting)
・以下テキスト
(会社概要・沿革・代表挨拶)
・下層ページへのリンクボタン

------

⑦フッター
サイト案内
------

⑧会社情報、ロゴ

以上になります。

ご不明点等がございましたらお気軽にお問い合わせ下さい。
何卒よろしくお願い申し上げます。
ページ数
1ページ
希望イメージ
• +5 0 +5
• シンプル
複雑
• 単色
カラフル
• 暗い
明るい
• 日常
高級
• 遊び心
厳粛
• 未来的
伝統的
• 女性的
男性的
希望する色
青系、水色系、グレー系、紫系
納品ファイル
• フォトショップ形式 (.psd)
補足説明
SD又は、FireworksPNGデータ
動画に関しましてはデータ添付またはURLをお送りいただけますと幸いです。
依頼公開後の追記内容
もう少し様々な作品を拝見させていただきたく、延長させていただきました。
引き続き、何卒よろしくお願いいたします。
■ 選んだ理由

全体の雰囲気が1番理想とするものに近く、構図も綺麗なバランスで組み立てられていました。
コーポレートサイトとしてシンプルかつおしゃれ見やすいものに仕上がると思い、korubin様の作品を選ばせていただきました。

■ 提案者全員のお礼・コメント

各ランサー様
この度は弊社へのコンペへご参加いただき、誠にありがとうございました。
どの作品も大変素晴らしく、当選させていただきたいアイディア、デザインがたくさんありました。
また機会がございましたら、作品をご投稿下さいますと幸いに存じます。
誠にありがとうございました。

```html
<!DOCTYPE html>
<html lang="ja">
<head>
<meta charset="utf-8">
<title>MiraKestel</title>
<link rel="stylesheet" href="https://fonts.googleapis.com/css2?family=Poiret+One&family=Josefin+Sans:wght@400;600&display=swap">
<style>
  :root {
    --mint: #cfe9e4;
    --mist: #eef4ef;
    --cream: #f3ead9;
    --sand: #c9b59c;
    --umber: #5a4033;
    --white: #ffffff;
    --peach: #f0b98a;
    --rust: #b4643f;
    --ink-soft: rgba(255,255,255,0.85);
  }
  html, body {
    margin: 0;
    padding: 0;
    width: 674px;
    height: 1200px;
    overflow: hidden;
    background: var(--mist);
  }
  .hero {
    position: relative;
    width: 674px;
    height: 1200px;
    overflow: hidden;
    font-family: "Josefin Sans", sans-serif;
  }
  .hero__visual {
    position: absolute;
    inset: 0;
    background:
      radial-gradient(ellipse 220px 300px at 560px 330px, rgba(70,50,40,0.55), transparent 70%),
      radial-gradient(ellipse 260px 420px at 560px 720px, rgba(246,238,224,0.95), transparent 75%),
      radial-gradient(ellipse 360px 260px at 200px 1080px, rgba(150,110,90,0.55), transparent 75%),
      linear-gradient(90deg, #bfe3dd 0%, #e3f1ec 35%, #f4efe4 65%, #e9dcc8 100%),
      linear-gradient(180deg, #f2f6f2 0%, #e6ece4 55%, #b9a592 100%);
    background-blend-mode: normal, normal, multiply, normal, multiply;
  }
  .hero__veil {
    position: absolute;
    inset: 0;
    background: linear-gradient(180deg, rgba(255,255,255,0.25) 0%, rgba(255,255,255,0) 40%, rgba(60,40,30,0.18) 100%);
  }
  .site-header {
    position: absolute;
    top: 0; left: 0; right: 0;
    height: 74px;
  }
  .brand {
    position: absolute;
    top: 26px;
    left: 50%;
    transform: translateX(-50%);
    display: flex;
    align-items: center;
    gap: 12px;
    color: var(--white);
    font-weight: 600;
    font-size: 24px;
    letter-spacing: 0.02em;
  }
  .brand__dot {
    width: 34px;
    height: 34px;
    border-radius: 50%;
    background: var(--white);
  }
  .menu-toggle {
    position: absolute;
    top: 0;
    right: 0;
    width: 108px;
    height: 74px;
    background: rgba(255,255,255,0.72);
    border: 0;
    padding: 0;
  }
  .menu-toggle span {
    position: absolute;
    left: 30px;
    width: 48px;
    height: 2px;
    background: var(--white);
    box-shadow: 0 0 1px rgba(0,0,0,0.15);
  }
  .menu-toggle span:nth-child(1) { top: 24px; }
  .menu-toggle span:nth-child(2) { top: 36px; }
  .menu-toggle span:nth-child(3) { top: 48px; }
  .headline {
    position: absolute;
    inset: 0;
    margin: 0;
  }
  .headline text {
    font-family: "Poiret One", sans-serif;
    font-size: 196px;
  }
  .stop-white { stop-color: var(--white); }
  .stop-peach { stop-color: var(--peach); }
  .stop-rust { stop-color: var(--rust); }
  .stop-umber { stop-color: var(--umber); }
  .scroll-cue {
    position: absolute;
    left: 50%;
    top: 1050px;
    transform: translateX(-50%);
    display: flex;
    flex-direction: column;
    align-items: center;
    color: var(--white);
  }
  .scroll-cue__mouse {
    width: 34px;
    height: 62px;
    border: 2px solid var(--white);
    border-radius: 17px;
    position: relative;
    box-sizing: border-box;
  }
  .scroll-cue__mouse::after {
    content: "";
    position: absolute;
    left: 50%;
    top: 14px;
    width: 2px;
    height: 12px;
    margin-left: -1px;
    background: var(--white);
  }
  .scroll-cue__label {
    margin-top: 14px;
    font-size: 14px;
    font-weight: 600;
    letter-spacing: 0.12em;
  }
  .scroll-cue__line {
    margin-top: 10px;
    width: 2px;
    height: 60px;
    background: var(--white);
  }
</style>
</head>
<body>
  <main class="hero">
    <div class="hero__visual" role="img" aria-label="Photo of a woman working on a laptop at a desk in a bright office"></div>
    <div class="hero__veil"></div>

    <svg class="headline" width="674" height="1200" viewBox="0 0 674 1200" aria-label="THIS DUMMY REPORT">
      <defs>
        <linearGradient id="tone-this" x1="0" y1="0" x2="1" y2="0">
          <stop offset="0" class="stop-white" stop-opacity="0.95"/>
          <stop offset="1" class="stop-white" stop-opacity="0.9"/>
        </linearGradient>
        <linearGradient id="tone-dummy" x1="0" y1="0" x2="1" y2="0">
          <stop offset="0" class="stop-white" stop-opacity="0.95"/>
          <stop offset="0.45" class="stop-white" stop-opacity="0.9"/>
          <stop offset="0.75" class="stop-peach"/>
          <stop offset="1" class="stop-rust"/>
        </linearGradient>
        <linearGradient id="tone-report" x1="0" y1="0" x2="1" y2="0">
          <stop offset="0" class="stop-rust"/>
          <stop offset="0.5" class="stop-umber"/>
          <stop offset="1" class="stop-rust"/>
        </linearGradient>
      </defs>
      <text x="12" y="452" textLength="404" lengthAdjust="spacingAndGlyphs" fill="url(#tone-this)">THIS</text>
      <text x="12" y="660" textLength="652" lengthAdjust="spacingAndGlyphs" fill="url(#tone-dummy)">DUMMY</text>
      <text x="12" y="905" textLength="652" lengthAdjust="spacingAndGlyphs" fill="url(#tone-report)" fill-opacity="0.85">REPORT</text>
    </svg>

    <header class="site-header">
      <div class="brand"><span class="brand__dot"></span>MiraKestel</div>
      <button class="menu-toggle" aria-label="Menu"><span></span><span></span><span></span></button>
    </header>

    <div class="scroll-cue">
      <div class="scroll-cue__mouse"></div>
      <div class="scroll-cue__label">SCROLL</div>
      <div class="scroll-cue__line"></div>
    </div>
  </main>
</body>
</html>
```